QDV Construction and Remodeling

Prefer a matte black card with some colors that pop, but subtle. Contact info. Show General Contractor professional way. Can you please remove renovations repairs maintenance off of my logo.

Target Market(s)

Property and business investors. Homeowners

Industry/Entity Type

Construction

Contact Information for Business Card

Name: Dorian Falkner, Title: CEO, Phone: 555-216-0394, Email: Dorian@QDVbuildTrx.com, website: www QDVbuildTrx.com

Font styles to use
Other font styles liked:
• Designer choose

Colors

Designer to choose colors to be used in the design.

Requirements
Must have
• Uniqueness. Double sided since it wont let me choose that. Professional look, be eye catching and catchy. QR code to my website
Nice to have
• Matte black background, subtle bright colors that pop, but I am open to anything. I also like black and gold with some red. Possible Harborton Ironclad logo colored stars somewhere around the logo or on the back. Just to rep my city
Should not have
• pink. Something you would see somewhere else. gif pictures or generated pictures.

```html
<!DOCTYPE html>
<html lang="en">
<head>
<meta charset="utf-8">
<title>QDV Construction and Remodeling – Business Card</title>
<link href="https://fonts.googleapis.com/css2?family=Lato:wght@400;700;900&display=swap" rel="stylesheet">
<style>
  :root {
    --page-bg: #ffffff;
    --card-black: #0b0b0c;
    --brand-red: #d7202a;
    --band-red-dark: #b51c24;
    --band-red-bright: #ea2029;
    --stripe-black: #0b0b0c;
    --name-red: #d42027;
    --tan: #e3cda9;
    --white: #ffffff;
  }
  * { margin: 0; padding: 0; box-sizing: border-box; }
  html, body {
    width: 1200px;
    height: 1200px;
    overflow: hidden;
    background: var(--page-bg);
    font-family: "Lato", sans-serif;
  }
  .sheet { position: relative; width: 1200px; height: 1200px; }

  .card {
    position: absolute;
    background: var(--card-black);
    box-shadow: 0 1px 3px rgba(0,0,0,0.25);
    overflow: hidden;
  }
  .card--front { left: 188px; top: 91px; width: 823px; height: 474px; }
  .card--back  { left: 186px; top: 635px; width: 828px; height: 474px; }

  .accent-band {
    position: absolute;
    left: 0; bottom: 0;
    width: 100%;
    height: 26px;
    background: linear-gradient(90deg, var(--band-red-dark) 0%, var(--band-red-bright) 55%, var(--band-red-dark) 100%);
  }
  .accent-band svg { position: absolute; left: 0; top: 0; width: 100%; height: 100%; }

  .wordmark {
    position: absolute;
    color: var(--white);
    font-weight: 900;
    text-transform: uppercase;
    line-height: 1;
    display: flex;
    align-items: center;
    gap: 14px;
  }
  .wordmark__square {
    width: 18px; height: 18px;
    background: var(--brand-red);
    flex: none;
  }
  .wordmark__name { display: flex; flex-direction: column; }
  .wordmark__initials { letter-spacing: 2px; }
  .wordmark__tagline { letter-spacing: 1.5px; margin-top: 6px; }

  .card--front .wordmark { left: 54px; top: 172px; }
  .card--front .wordmark__initials { font-size: 78px; }
  .card--front .wordmark__tagline { font-size: 15px; }

  .card--back .wordmark { left: 198px; top: 158px; gap: 20px; }
  .card--back .wordmark__square { width: 26px; height: 26px; }
  .card--back .wordmark__initials { font-size: 118px; }
  .card--back .wordmark__tagline { font-size: 22px; margin-top: 10px; letter-spacing: 2px; }

  .divider {
    position: absolute;
    left: 411px; top: 156px;
    width: 2px; height: 163px;
    background: var(--brand-red);
  }

  .identity { position: absolute; left: 455px; top: 152px; }
  .identity__name {
    font-size: 35px;
    font-weight: 700;
    color: var(--name-red);
    text-transform: uppercase;
    letter-spacing: 0.2px;
    line-height: 1;
  }
  .identity__title {
    font-size: 20px;
    font-weight: 400;
    color: var(--tan);
    margin-top: 10px;
    line-height: 1;
  }

  .contact-list { position: absolute; left: 453px; top: 238px; list-style: none; }
  .contact-list__item {
    display: flex;
    align-items: center;
    height: 30px;
    font-size: 20px;
    color: var(--tan);
  }
  .contact-list__icon { width: 20px; height: 20px; margin-right: 13px; flex: none; }
</style>
</head>
<body>
<div class="sheet">

  <section class="card card--front" aria-label="Business card front">
    <div class="wordmark">
      <span class="wordmark__square"></span>
      <span class="wordmark__name">
        <span class="wordmark__initials">QDV</span>
        <span class="wordmark__tagline">Construction &amp; Remodeling</span>
      </span>
    </div>

    <div class="divider"></div>

    <div class="identity">
      <h1 class="identity__name">Dorian Falkner</h1>
      <p class="identity__title">CEO</p>
    </div>

    <ul class="contact-list">
      <li class="contact-list__item">
        <svg class="contact-list__icon" viewBox="0 0 24 24" aria-hidden="true">
          <path fill="#d7202a" d="M6.6 10.8c1.4 2.8 3.8 5.1 6.6 6.6l2.2-2.2c.3-.3.7-.4 1-.2 1.1.4 2.3.6 3.6.6.6 0 1 .4 1 1V20c0 .6-.4 1-1 1C10.6 21 3 13.4 3 4c0-.6.4-1 1-1h3.5c.6 0 1 .4 1 1 0 1.3.2 2.5.6 3.6.1.3 0 .7-.2 1L6.6 10.8z"/>
        </svg>
        555-216-0394
      </li>
      <li class="contact-list__item">
        <svg class="contact-list__icon" viewBox="0 0 24 24" aria-hidden="true">
          <rect x="2" y="5" width="20" height="14" fill="#d7202a"/>
          <path d="M2 5l10 8 10-8M2 19l7-7M22 19l-7-7" fill="none" stroke="#0b0b0c" stroke-width="1.6"/>
        </svg>
        Dorian@QDVbuildTrx.com
      </li>
      <li class="contact-list__item">
        <svg class="contact-list__icon" viewBox="0 0 24 24" aria-hidden="true">
          <g fill="none" stroke="#d7202a" stroke-width="1.8">
            <circle cx="12" cy="12" r="9.5"/>
            <ellipse cx="12" cy="12" rx="4.2" ry="9.5"/>
            <path d="M2.5 12h19M4 7h16M4 17h16"/>
          </g>
        </svg>
        www QDVbuildTrx.com
      </li>
    </ul>

    <div class="accent-band">
      <svg viewBox="0 0 823 26" preserveAspectRatio="none" aria-hidden="true">
        <polygon points="346,26 360,26 392,0 378,0" fill="#0b0b0c"/>
        <polygon points="381,26 395,26 427,0 413,0" fill="#0b0b0c"/>
        <polygon points="416,26 430,26 462,0 448,0" fill="#0b0b0c"/>
      </svg>
    </div>
  </section>

  <section class="card card--back" aria-label="Business card back">
    <div class="wordmark">
      <span class="wordmark__square"></span>
      <span class="wordmark__name">
        <span class="wordmark__initials">QDV</span>
        <span class="wordmark__tagline">Construction &amp; Remodeling</span>
      </span>
    </div>

    <div class="accent-band">
      <svg viewBox="0 0 828 26" preserveAspectRatio="none" aria-hidden="true">
        <polygon points="350,0 364,0 396,26 382,26" fill="#0b0b0c"/>
        <polygon points="385,0 399,0 431,26 417,26" fill="#0b0b0c"/>
        <polygon points="420,0 434,0 466,26 452,26" fill="#0b0b0c"/>
      </svg>
    </div>
  </section>

</div>
</body>
</html>
```